Law Office needs stationery design and business card

I currently have been using the same letterhead for the last 8 years. Since i 'm about to adding another location, I want to revamp my letterhead and business card. I already have a logo i'm happy with. I will upload my current letterhead, fax sheet, envelope, and logos. I need a business card also. I have 2 locations, 1 phone number, 1 fax line, website, etc. If possible and fitting with the design, I would like to keep the same information listed currently on the letterhead.

**Keep in mind, I also NEED A FAX SHEET COVER. thank you

Hello, Please submit a Gray Scale or Black and White version of your designs also, since most of the time I will be printing NON color stationery. I will seldom use a color print for my letterhead, I would like to have a color version for my benefit, however i will print in grayscale majority of the time . For the Business Card, that can just be in color. When I get my business cards they will be in color.Thank youEnrique Added Sunday, September 18, 2016

```html
<!DOCTYPE html>
<html lang="en">
<head>
<meta charset="utf-8">
<title>Marlowe Law – Letterhead</title>
<link href="https://fonts.googleapis.com/css2?family=Cormorant+Garamond:wght@500&family=Tenor+Sans&display=swap" rel="stylesheet">
<style>
  :root {
    --paper: #ffffff;
    --mark-grey: #b3b3b3;
    --name-grey: #8c8c8c;
    --rule-grey: #b5b5b5;
    --contact-ink: #5a5a5a;
  }
  html, body {
    margin: 0;
    padding: 0;
    overflow: hidden;
    background: var(--paper);
  }
  .letterhead {
    position: relative;
    width: 849px;
    height: 1200px;
    background: var(--paper);
    overflow: hidden;
  }
  .brand {
    position: absolute;
    top: 88px;
    left: 0;
    width: 100%;
    display: flex;
    flex-direction: column;
    align-items: center;
  }
  .brand-square {
    width: 96px;
    height: 96px;
    background: var(--mark-grey);
    margin-bottom: 36px;
  }
  .brand-name {
    margin: 0;
    font-family: "Cormorant Garamond", Georgia, serif;
    font-weight: 500;
    font-size: 36px;
    letter-spacing: 0.5px;
    color: var(--name-grey);
    line-height: 1;
  }
  .footer {
    position: absolute;
    top: 1118px;
    left: 0;
    width: 100%;
    display: flex;
    flex-direction: column;
    align-items: center;
  }
  .footer-rule {
    display: block;
    width: 312px;
    height: 8px;
  }
  .contact {
    margin: 14px 0 0;
    font-family: "Tenor Sans", "Optima", sans-serif;
    font-style: normal;
    font-size: 13px;
    line-height: 21px;
    letter-spacing: 0.6px;
    color: var(--contact-ink);
    text-align: center;
  }
</style>
</head>
<body>
  <main class="letterhead">
    <header class="brand">
      <div class="brand-square"></div>
      <h1 class="brand-name">MARLOWE LAW</h1>
    </header>

    <footer class="footer">
      <svg class="footer-rule" viewBox="0 0 312 8" aria-hidden="true">
        <line x1="4" y1="4" x2="308" y2="4" stroke="var(--rule-grey)" stroke-width="2"/>
        <circle cx="4" cy="4" r="3.5" fill="var(--rule-grey)"/>
        <circle cx="308" cy="4" r="3.5" fill="var(--rule-grey)"/>
      </svg>
      <address class="contact">
        418 East Elm St., Suite 200<br>
        Fairview, PA 19000, (555)010.2274
      </address>
    </footer>
  </main>
</body>
</html>
```